Business card design for crowd sourced review site.

I need a business card magnet design for an online, crowd-sourced, restaurant review site strictly for Kosher restaurants.
It is similar to RoamLedger but catering to a very particular crowd.
The markets it will be distributed in are flooded with business card fridge magnets so this needs to be eye-catching and unique. The Business name is PlateMarks
The website isnt finished but you can see the basic setup here
http://restaurant.vintrello.com/

The second image i included is another logo design I liked and was thinking about using and decided I will probably also make a SECOND custom cut business card in the shape of that icon. Bonus if you can throw that in also.

Target Market(s)

Jewish consumers aged 20-35

Industry/Entity Type

Business

Contact Information for Business Card

see description.
Design should not be too crowded and should in eye-catching. Will mainly be used as fridge magnets.

Requirements
Must have
• Website address. logo.
Nice to have
• tagline. (The Definitive guide to kosher dining for the Kosher consumer)
• Im not a professional but I personally think the color blue goes along with this concept. ill leave it to you to decide.
Should not have
• any religious symbols.

```html
<!DOCTYPE html>
<html lang="en">
<head>
<meta charset="utf-8">
<title>PlateMarks Business Card</title>
<link rel="stylesheet" href="https://fonts.googleapis.com/css2?family=Open+Sans:wght@400;600&display=swap">
<style>
  :root {
    --page-bg: #d6d6d6;
    --card-white: #f4f4f4;
    --accent-orange: #e2572a;
    --text-dark: #3a3a3a;
    --icon-white: #ffffff;
  }
  * { box-sizing: border-box; margin: 0; padding: 0; }
  html, body {
    width: 1200px;
    height: 1200px;
    overflow: hidden;
    background: var(--page-bg);
    font-family: "Open Sans", Arial, sans-serif;
  }
  .stage {
    width: 1200px;
    height: 1200px;
    display: flex;
    align-items: center;
    justify-content: center;
  }
  .business-card {
    position: relative;
    width: 1000px;
    height: 572px;
    background: var(--card-white);
    overflow: hidden;
    box-shadow: 0 6px 18px rgba(0,0,0,0.18);
  }
  .card-wedges {
    position: absolute;
    inset: 0;
    width: 100%;
    height: 100%;
  }
  .card-wedges path { fill: var(--accent-orange); }
  .brand {
    position: absolute;
    left: 350px;
    top: 96px;
    display: flex;
    align-items: center;
    gap: 22px;
  }
  .brand-dot {
    width: 64px;
    height: 64px;
    border-radius: 50%;
    background: var(--accent-orange);
  }
  .brand-name {
    font-size: 64px;
    font-weight: 600;
    color: var(--accent-orange);
    letter-spacing: -0.5px;
  }
  .contact-block {
    position: absolute;
    left: 220px;
    top: 330px;
    color: var(--text-dark);
  }
  .contact-name {
    font-size: 36px;
    font-weight: 400;
    margin-bottom: 22px;
  }
  .contact-list { list-style: none; }
  .contact-item {
    display: flex;
    align-items: center;
    gap: 16px;
    font-size: 28px;
    line-height: 1;
    margin-bottom: 14px;
  }
  .contact-icon {
    width: 28px;
    height: 28px;
    flex: none;
  }
  .contact-icon rect { fill: var(--accent-orange); }
  .contact-icon .glyph { fill: none; stroke: var(--icon-white); stroke-width: 2; }
  .contact-icon .glyph-fill { fill: var(--icon-white); }
</style>
</head>
<body>
<main class="stage">
  <article class="business-card">
    <svg class="card-wedges" viewBox="0 0 1000 572" preserveAspectRatio="none" aria-hidden="true">
      <path d="M0 0 L230 0 Q150 150 120 330 L0 330 Z"/>
      <path d="M0 330 L120 330 Q100 400 90 572 L0 572 Z" fill="none"/>
      <path d="M880 0 L1000 0 L1000 572 L960 572 Q920 300 880 0 Z"/>
    </svg>

    <div class="brand">
      <span class="brand-dot"></span>
      <span class="brand-name">PlateMarks</span>
    </div>

    <section class="contact-block">
      <h2 class="contact-name">Miriam</h2>
      <ul class="contact-list">
        <li class="contact-item">
          <svg class="contact-icon" viewBox="0 0 28 28" aria-hidden="true">
            <rect width="28" height="28" rx="4"/>
            <path class="glyph" d="M7 11 Q14 5 21 11 L19 13 L17 11 L11 11 L9 13 Z"/>
            <rect class="glyph-fill" x="9" y="14" width="10" height="7" rx="1" style="fill:#fff"/>
          </svg>
          <span>0451 287 934</span>
        </li>
        <li class="contact-item">
          <svg class="contact-icon" viewBox="0 0 28 28" aria-hidden="true">
            <rect width="28" height="28" rx="4"/>
            <rect class="glyph" x="9" y="5" width="10" height="18" rx="2"/>
            <circle class="glyph-fill" cx="14" cy="20" r="1.3"/>
          </svg>
          <span>7063918275</span>
        </li>
        <li class="contact-item">
          <svg class="contact-icon" viewBox="0 0 28 28" aria-hidden="true">
            <rect width="28" height="28" rx="4"/>
            <circle class="glyph" cx="14" cy="14" r="8"/>
            <path class="glyph" d="M6 14 H22 M14 6 Q9 14 14 22 M14 6 Q19 14 14 22"/>
          </svg>
          <span>www.restaurant.vintrello.com</span>
        </li>
      </ul>
    </section>
  </article>
</main>
</body>
</html>
```